Locksmith Store 474747 Signage

Design Brief: Locksmith Store Signage – "Locksmith 474747" [ΚΛΕΙΔΑΡΑΣ 474747 (in Greek)]
We are looking for a spectacular and professional sign design for the exterior of our locksmith store.
Signage Dimensions:
• Width: 6 meters
• Height: 1.5 meters
• Shopfront window Width: 6 meters, Height: 2.5 meters
Key Requirements (in order of importance):
1. It must be immediately clear that this is a locksmith store. [ΚΛΕΙΔΑΡΑΣ (in Greek)]
2. The store name "474747", (which is also the phone number 2310474747), should be highly visible and visually striking because this is the number that customers are calling when they are locked out.
3. The signage should also clearly communicate that except for house keys, which is obvious for a locksmith store the services we provide are:
o All kinds of house keys. ΚΛΕΙΔΙΑ ΣΠΙΤΙΩΝ(in Greek) (There is no key that we cannot do)
o Immobiliser car keys = ΚΛΕΙΔΙΑ ΑΥΤΟΚΙΝΗΤΩΝ (in Greek)
We unlock every car that exist, we program new immobilizer keys – remote controls, even if all keys are lost, we repair or change broken cells of car keys, we change batteries.
o High-security locks = ΚΛΕΙΔΑΡΙΕΣ ΑΣΦΑΛΕΙΑΣ (in Greek) we sell the best high security locks in the planet
o Armoured doors = ΠΟΡΤΕΣ ΑΣΦΑΛΕΙΑΣ (in Greek) (this may not be so important to be on the signage.
Visual Style:
We are open to creative direction, but the design should be eye-catching, professional, and modern, something that will stand out on a busy street and instantly tell customers who we are and what we offer. Also, you may use the shopfront window for graphic designs. Also, we are open if a part of the signage is digital.
________________________________________
Updates
Hello Designers,
Thank you so much for your effort and the designs you've shared.
I realized I forgot to mention that you can refer to my website at www.474747-keys.example.gr for more context.
Additionally, I’ve just uploaded two new photos: one showing the store with a black outline at the dimensions of the signage, and another with the large double-bit key placed in a different position to demonstrate that it is moveable.
Thanks again for your dedication!
Target Market(s)
every person that has a key
Look and feel
Each slider illustrates characteristics of the customer's brand and the style your logo design should communicate.

```html
<!DOCTYPE html>
<html lang="el">
<head>
<meta charset="utf-8">
<title>ΚΛΕΙΔΑΡΑΣ 474747 – Signage</title>
<link href="https://fonts.googleapis.com/css2?family=Montserrat:wght@800&family=Open+Sans:wght@700;800&family=Orbitron:wght@900&display=swap" rel="stylesheet">
<style>
  :root {
    --backdrop: #2c2d30;
    --panel: #050505;
    --gold-light: #fff1a8;
    --gold: #e9b53a;
    --gold-deep: #a86f10;
    --silver-light: #ffffff;
    --silver: #b9b9bd;
    --silver-deep: #6d6d72;
    --text-white: #ffffff;
  }
  * { margin: 0; padding: 0; box-sizing: border-box; }
  html, body {
    width: 1200px; height: 750px; overflow: hidden;
    background: var(--backdrop);
  }
  .sign {
    position: absolute; left: 20px; top: 236px;
    width: 1160px; height: 277px;
    background: var(--panel);
    overflow: hidden;
    box-shadow: 0 8px 18px rgba(0,0,0,.55);
  }
  .sign-backdrop { position: absolute; inset: 0; width: 100%; height: 100%; }
  .trade-title {
    position: absolute; left: 190px; top: 70px;
    font-family: "Open Sans", sans-serif; font-weight: 800;
    font-size: 64px; line-height: 1;
    background: linear-gradient(180deg, var(--silver-light) 0%, var(--silver) 55%, var(--silver-deep) 100%);
    -webkit-background-clip: text; background-clip: text; color: transparent;
    filter: drop-shadow(0 3px 2px rgba(0,0,0,.9));
  }
  .store-number {
    position: absolute; left: 138px; top: 138px;
    font-family: "Orbitron", sans-serif; font-weight: 900;
    font-size: 68px; line-height: 1; letter-spacing: 2px;
    background: linear-gradient(180deg, var(--gold-light) 0%, var(--gold) 50%, var(--gold-deep) 100%);
    -webkit-background-clip: text; background-clip: text; color: transparent;
    filter: drop-shadow(0 0 8px rgba(233,181,58,.55)) drop-shadow(0 3px 2px rgba(0,0,0,.9));
  }
  .phone-line {
    position: absolute; left: 703px; top: 41px;
    display: flex; align-items: center; gap: 12px;
  }
  .phone-icon { width: 47px; height: 47px; flex: none; }
  .phone-number {
    font-family: "Montserrat", sans-serif; font-weight: 800;
    font-size: 50px; line-height: 1;
    background: linear-gradient(180deg, var(--silver-light) 0%, var(--silver) 60%, var(--silver-deep) 100%);
    -webkit-background-clip: text; background-clip: text; color: transparent;
    filter: drop-shadow(0 2px 2px rgba(0,0,0,.9));
  }
  .service-list {
    position: absolute; left: 722px; top: 106px;
    list-style: none;
    font-family: "Open Sans", sans-serif; font-weight: 700;
    font-size: 29px; line-height: 37px; color: var(--text-white);
  }
  .service-list li { display: flex; align-items: center; gap: 7px; }
  .service-list li::before {
    content: ""; width: 0; height: 0;
    border-top: 8px solid transparent; border-bottom: 8px solid transparent;
    border-left: 8px solid var(--gold);
  }
  .key-art { position: absolute; }
  .key-art--left {
    left: 20px; top: 176px; width: 150px; height: 130px;
    background: radial-gradient(closest-side, rgba(233,181,58,.5), rgba(170,170,175,.18) 55%, rgba(0,0,0,0) 100%);
  }
  .key-art--right {
    left: 552px; top: 166px; width: 152px; height: 140px;
    background: radial-gradient(closest-side, rgba(233,181,58,.5), rgba(170,170,175,.18) 55%, rgba(0,0,0,0) 100%);
  }
</style>
</head>
<body>
  <div class="sign">
    <svg class="sign-backdrop" viewBox="0 0 1160 277" preserveAspectRatio="none">
      <defs>
        <linearGradient id="goldBand" x1="0" y1="0" x2="1" y2="1">
          <stop offset="0" stop-color="#7a4f0c"/>
          <stop offset=".5" stop-color="#ffd86a"/>
          <stop offset="1" stop-color="#8a5a10"/>
        </linearGradient>
        <linearGradient id="waveGlow" x1="0" y1="0" x2="1" y2="0">
          <stop offset="0" stop-color="#c9962e" stop-opacity="0"/>
          <stop offset=".4" stop-color="#c9962e" stop-opacity=".28"/>
          <stop offset="1" stop-color="#c9962e" stop-opacity=".12"/>
        </linearGradient>
      </defs>
      <path role="img" aria-label="Flowing gold line-wave pattern with gold sparkles"
            d="M150 0 H1160 V150 C1050 70 900 40 800 60 C700 80 690 200 620 200 C560 200 520 40 420 40 C320 40 250 30 150 0 Z"
            fill="url(#waveGlow)"/>
      <g class="corner-bands corner-bands--top">
        <polygon points="0,96 150,0 165,0 0,106" fill="url(#goldBand)"/>
        <polygon points="0,112 174,0 200,0 0,128" fill="url(#goldBand)"/>
        <polygon points="0,134 208,0 218,0 0,141" fill="url(#goldBand)" opacity=".8"/>
      </g>
      <g class="corner-bands corner-bands--bottom">
        <polygon points="1160,150 1160,160 980,277 965,277" fill="url(#goldBand)" opacity=".8"/>
        <polygon points="1160,168 1160,186 1020,277 992,277" fill="url(#goldBand)"/>
        <polygon points="1160,196 1160,206 1046,277 1031,277" fill="url(#goldBand)"/>
      </g>
    </svg>

    <div class="key-art key-art--left" role="img" aria-label="Silver and gold keys illustration"></div>
    <div class="key-art key-art--right" role="img" aria-label="Gold and silver antique keys illustration"></div>

    <h1 class="trade-title">ΚΛΕΙΔΑΡΑΣ</h1>
    <div class="store-number">474.747</div>

    <div class="phone-line">
      <svg class="phone-icon" viewBox="0 0 48 48" aria-hidden="true">
        <defs>
          <linearGradient id="iconGold" x1="0" y1="0" x2="0" y2="1">
            <stop offset="0" stop-color="#ffe08a"/>
            <stop offset="1" stop-color="#b97a12"/>
          </linearGradient>
        </defs>
        <circle cx="24" cy="24" r="23" fill="url(#iconGold)"/>
        <path d="M16 12c1.5-1 3-.5 3.6.8l2 4c.5 1 .2 2-.6 2.7l-1.6 1.3c1 2.6 3.2 4.8 5.8 5.8l1.3-1.6c.7-.8 1.7-1.1 2.7-.6l4 2c1.300.6 1.8 2.1.8 3.6l-1.4 2c-1 1.4-2.8 2-4.4 1.4C20.6 33 15 27.4 13 19.8c-.5-1.6 0-3.4 1.4-4.4z" fill="#1a1206"/>
      </svg>
      <span class="phone-number">2310474747</span>
    </div>

    <ul class="service-list">
      <li>ΚΛΕΙΔΙΑ ΣΠΙΤΙΩΝ</li>
      <li>ΚΛΕΙΔΙΑ ΑΥΤΟΚΙΝΗΤΩΝ</li>
      <li>ΚΛΕΙΔΑΡΙΕΣ ΑΣΦΑΛΕΙΑΣ</li>
      <li>ΠΟΡΤΕΣ ΑΣΦΑΛΕΙΑΣ</li>
    </ul>
  </div>
</body>
</html>
```